Poster announcing University Web Analytics talk

We need a poster to announce an upcoming talk on Web Analytics at the local University. The event is addressed to final year students (mostly in Informatic Engineering, although other majors are wellcomed as well) who may be interested in specializing in this rising field.

The poster should present a brief list of the points we'll be addressing, as well as the place and time of the meeting. Also, it must feature our company logo (check the uploads section to find it) and our website url: http://www.brasslanternworks.net.

Texts for the poster:

Headline: "Get specialized in Web & Mobile Analytics"

Topics that will be covered:
- Introduction to Analytics, market, work opportunities
- Know the basics of an Analytics project: planning, phases, implementation
- Job bank: bring your CV!

Event information: "Thursday 20th June at the Escuela de Sistemas, Instituto Pelayo Norte". [A space to fill with the time must be provided here]

However, we'll be translating all the text to Spanish later, so we'll need a file where we can modify the text layers.
Updates

Thanks to all of you, we're receiving so many excellent works!

We had missed to include some important information on the brief - we didn't say anything about the colors, and we have been getting some designs based in dark colors. Now, it doesn't matter what colors you use, but we'd like better a brighter design (no matter if the color combination is more playful or either rather serious). This is going to be a free talk addressed to last year students, so we want to transmit a feeling of an interesting, easy and entertaining afternoon.

I hope these comments are helpful, please reach me with any question or comment. 

Thanks a lot again!
Nuria 
BL team

Target Market(s)

Final year students and graduates.

Industry/Entity Type

Bank

Requirements
Must have
• Design must be submitted in vector format, preferably .psd. We must be able to modify the text layers. Our logo (check the files section) and website url (http://www.brasslanternworks.net) must be included
Nice to have
• Illustrations making reference to Analytics (charts, statistics, code) and/or the internet will be a plus!

```html
<!DOCTYPE html>
<html lang="en">
<head>
<meta charset="utf-8">
<title>Get Specialized in Web &amp; Mobile Analytics</title>
<link rel="stylesheet" href="https://fonts.googleapis.com/css2?family=Jost:wght@300;400;600&family=Oswald:wght@500;600&display=swap">
<style>
  :root {
    --sky-deep: #0a4763;
    --sky-mid: #2a7c9f;
    --sky-pale: #dbeef3;
    --sky-mist: #f0f7f9;
    --cloud-top: #0c416e;
    --cloud-bottom: #1d6fa7;
    --cloud-edge: #08304f;
    --tail-light: #0a8ccc;
    --tail-dark: #0b5b92;
    --ink-white: #ffffff;
    --ink-navy: #0d4a6a;
    --brand: #11506f;
  }
  * { margin: 0; padding: 0; box-sizing: border-box; }
  html, body { width: 790px; height: 1200px; overflow: hidden; }
  body { background: var(--sky-mist); }
  .poster {
    position: relative;
    width: 790px;
    height: 1200px;
    overflow: hidden;
    background: linear-gradient(180deg, var(--sky-deep) 0%, #135a78 22%, var(--sky-mid) 42%, var(--sky-pale) 66%, var(--sky-mist) 100%);
    font-family: "Jost", "Futura", sans-serif;
  }
  .backdrop-scene {
    position: absolute;
    left: 0; top: 0;
    width: 790px; height: 1200px;
    background:
      radial-gradient(ellipse 420px 300px at 470px 260px, rgba(255,255,255,0.10), transparent 70%),
      linear-gradient(180deg, transparent 72%, rgba(150,160,170,0.25) 82%, rgba(180,188,196,0.18) 100%);
  }
  .speaker-profile {
    position: absolute;
    left: 0; top: 515px;
    width: 215px; height: 545px;
    border-radius: 0 130px 100px 0;
    background: linear-gradient(90deg, #f4f6f7 0%, #e9edef 72%, #151515 73%, #111 100%);
  }
  .speech-bubble { position: absolute; left: 0; top: 0; }
  .headline {
    position: absolute;
    top: 26px; left: 0; width: 790px;
    text-align: center;
    color: var(--ink-white);
  }
  .headline-lead {
    display: block;
    font-weight: 300;
    font-size: 53px;
    line-height: 52px;
    letter-spacing: 1px;
  }
  .headline-main {
    display: block;
    font-family: "Oswald", "Arial Narrow", sans-serif;
    font-weight: 600;
    font-size: 50px;
    line-height: 56px;
    letter-spacing: 0.5px;
  }
  .topics-title {
    position: absolute;
    top: 210px; left: 0; width: 790px;
    text-align: center;
    color: var(--ink-white);
    font-weight: 300;
    font-size: 36px;
    letter-spacing: 1px;
  }
  .topic-list { list-style: none; }
  .topic {
    position: absolute;
    color: var(--ink-white);
    font-family: "Oswald", "Arial Narrow", sans-serif;
    font-weight: 500;
    font-size: 26px;
    line-height: 36px;
    letter-spacing: 0.3px;
    white-space: nowrap;
  }
  .topic-marker {
    display: inline-block;
    width: 26px; height: 18px;
    margin-right: 6px;
    vertical-align: 2px;
  }
  .topic-intro { left: 88px; top: 295px; }
  .topic-basics { left: 153px; top: 386px; }
  .topic-basics .topic-line2 { display: block; padding-left: 67px; }
  .topic-jobs { left: 228px; top: 526px; }
  .event-details {
    position: absolute;
    left: 481px; top: 701px;
    color: var(--ink-navy);
    font-size: 16px;
    line-height: 25px;
  }
  .event-row { margin-bottom: 44px; }
  .event-row.place { margin-top: -8px; }
  .event-value { font-weight: 600; }
  .brand-mark {
    position: absolute;
    left: 482px; top: 1078px;
    display: flex; align-items: center; gap: 12px;
  }
  .brand-square { width: 58px; height: 58px; background: var(--brand); }
  .brand-name {
    font-weight: 600;
    font-size: 36px;
    line-height: 38px;
    color: var(--brand);
  }
  .brand-url {
    position: absolute;
    left: 482px; top: 1164px;
    font-size: 14px;
    color: var(--brand);
  }
</style>
</head>
<body>
<main class="poster">
  <div class="backdrop-scene" role="img" aria-label="Faint globe with orbit rings and silhouettes of business people shaking hands"></div>

  <div class="speaker-profile" role="img" aria-label="Black and white profile silhouette of a speaking head"></div>

  <svg class="speech-bubble" width="790" height="1200" viewBox="0 0 790 1200" aria-hidden="true">
    <defs>
      <linearGradient id="cloudFill" x1="0" y1="0" x2="0" y2="1">
        <stop offset="0" stop-color="var(--cloud-top)"/>
        <stop offset="1" stop-color="var(--cloud-bottom)"/>
      </linearGradient>
      <linearGradient id="tailFill" x1="0" y1="0" x2="1" y2="1">
        <stop offset="0" stop-color="var(--tail-light)"/>
        <stop offset="1" stop-color="var(--tail-dark)"/>
      </linearGradient>
    </defs>
    <path d="M350 600 C 362 800, 300 950, 172 1056 C 265 1000, 395 860, 418 600 Z" fill="url(#tailFill)"/>
    <path class="cloud" fill="url(#cloudFill)" fill-opacity="0.9" stroke="var(--cloud-edge)" stroke-opacity="0.5" stroke-width="4"
      d="M140 425
         C 55 395, 50 245, 175 222
         C 205 150, 330 128, 405 160
         C 480 125, 610 145, 628 218
         C 745 225, 765 385, 665 425
         C 730 470, 705 600, 590 605
         C 545 640, 465 632, 420 612
         C 380 642, 300 642, 250 605
         C 125 612, 55 485, 140 425 Z"/>
  </svg>

  <h1 class="headline">
    <span class="headline-lead">GET SPECIALIZED IN</span>
    <span class="headline-main">WEB &amp; MOBILE ANALYTICS</span>
  </h1>

  <h2 class="topics-title">TOPICS</h2>

  <ul class="topic-list">
    <li class="topic topic-intro"><svg class="topic-marker" viewBox="0 0 20 14"><ellipse cx="8" cy="7" rx="7" ry="6" fill="#fff"/><path d="M13 9 L20 12 L12 12 Z" fill="#fff"/></svg>Introduction to Analytics, market, work opportunities</li>
    <li class="topic topic-basics"><svg class="topic-marker" viewBox="0 0 20 14"><ellipse cx="8" cy="7" rx="7" ry="6" fill="#fff"/><path d="M13 9 L20 12 L12 12 Z" fill="#fff"/></svg>Know the basics of an Analytics project:<span class="topic-line2">planning, phases, implementation</span></li>
    <li class="topic topic-jobs"><svg class="topic-marker" viewBox="0 0 20 14"><ellipse cx="8" cy="7" rx="7" ry="6" fill="#fff"/><path d="M13 9 L20 12 L12 12 Z" fill="#fff"/></svg>Job bank: bring your CV!</li>
  </ul>

  <section class="event-details">
    <p class="event-row"><span class="event-label">Date: </span><span class="event-value">Thursday 20th June</span></p>
    <p class="event-row"><span class="event-label">Time: </span><span class="event-value">10.00am</span></p>
    <p class="event-row place"><span class="event-label">Place: </span><span class="event-value">Escuela de Sistemas,<br>Instituto Pelayo Norte</span></p>
  </section>

  <div class="brand-mark">
    <span class="brand-square"></span>
    <span class="brand-name">brass lantern<br>works</span>
  </div>
  <p class="brand-url">http://www.brasslanternworks.net</p>
</main>
</body>
</html>
```